ebook cover: book 4 in the We Hum Lantern series. Lantern by Riverside

I am wanting a striking cover to bring the forth book in a spiritual journey series to an audience ready to meet new characters and get excited again! White backgrounds, red titles (any font), subtitles to introduce a new major character in the series of ten (same fonts please as the original, We Hum Lantern), and one emblematic, slightly mysterious image. Please keep to the same colour tones as the original, but the lead image need not be gray. Let's please try to use the "light flash" that is on the tin can in We Hum Lantern somehow, in your own way. It is meant to signify the other side, or the higher light, or some such inference.

Book details:
Title: Lantern by Riverside
Subtitle: Archangel Veloriel brings the message
Image: silver hourglass
Author: Maren Tulliver, Ph.D
Strap quote: "Tulliver is smart, savvy and full of ideas," Harbourgate Ledger

Please do your best: this one is going in competition of spiritual healers!

Thanks! :)

```html
<!DOCTYPE html>
<html lang="en">
<head>
<meta charset="utf-8">
<title>Lantern by Riverside — Book Cover</title>
<link rel="stylesheet" href="https://fonts.googleapis.com/css2?family=Playfair+Display:wght@800&family=Open+Sans:wght@300;400;600&display=swap">
<style>
  :root {
    --paper: #ffffff;
    --title-red: #b3121a;
    --ink: #262626;
    --author-grey: #6b6b6b;
    --silver-light: #f2f2f2;
    --silver-mid: #c9c9c9;
    --silver-dark: #8e8e8e;
  }
  * { margin: 0; padding: 0; box-sizing: border-box; }
  html, body {
    width: 800px;
    height: 1200px;
    overflow: hidden;
    background: var(--paper);
  }
  .cover {
    position: relative;
    width: 800px;
    height: 1200px;
    background: var(--paper);
    font-family: "Open Sans", Arial, sans-serif;
  }
  .strap-quote {
    position: absolute;
    top: 36px;
    left: 0;
    width: 800px;
    text-align: center;
    font-size: 13px;
    font-weight: 600;
    color: var(--ink);
    letter-spacing: 0.2px;
    text-transform: uppercase;
  }
  .strap-quote .source {
    font-size: 16px;
    letter-spacing: 0.5px;
  }
  .title {
    position: absolute;
    top: 78px;
    left: 0;
    width: 800px;
    text-align: center;
    font-family: "Playfair Display", "Times New Roman", serif;
    font-weight: 800;
    color: var(--title-red);
    text-transform: uppercase;
    font-size: 132px;
    line-height: 106px;
  }
  .title-line {
    display: block;
    transform: scaleX(0.74);
    transform-origin: center;
    white-space: nowrap;
  }
  .subtitle {
    position: absolute;
    top: 350px;
    left: 0;
    width: 800px;
    text-align: center;
    font-size: 33px;
    font-weight: 400;
    line-height: 50px;
    letter-spacing: 4px;
    color: var(--ink);
    text-transform: uppercase;
  }
  .lead-image {
    position: absolute;
    left: 255px;
    top: 555px;
    width: 290px;
    height: 420px;
  }
  .author {
    position: absolute;
    top: 1048px;
    left: 0;
    width: 800px;
    text-align: center;
    font-size: 44px;
    font-weight: 300;
    letter-spacing: 5px;
    color: var(--author-grey);
    text-transform: uppercase;
  }
</style>
</head>
<body>
  <main class="cover">
    <p class="strap-quote">"Tulliver is smart, savvy and full of ideas" - <span class="source">Harbourgate Ledger</span></p>

    <h1 class="title">
      <span class="title-line">Lantern by</span>
      <span class="title-line">Riverside</span>
    </h1>

    <h2 class="subtitle">Archangel Veloriel<br>brings the message</h2>

    <svg class="lead-image" viewBox="0 0 290 420" role="img" aria-label="Silver hourglass with white sand and a light flash at its top rim">
      <defs>
        <linearGradient id="silver-tone" x1="0" y1="0" x2="1" y2="0">
          <stop offset="0" stop-color="var(--silver-dark)"/>
          <stop offset="0.45" stop-color="var(--silver-light)"/>
          <stop offset="1" stop-color="var(--silver-mid)"/>
        </linearGradient>
      </defs>
      <rect x="0" y="0" width="290" height="420" rx="12" fill="url(#silver-tone)" opacity="0.55"/>
    </svg>

    <p class="author">Maren Tulliver Ph.D.</p>
  </main>
</body>
</html>
```